Steadfast Property Reviews

We need stationery for our new home inspection company. We inspect homes for people prior to purchasing to ensure the property is in good condition, as well as inspecting new homes to ensure they have been built to the appropriate standards. We are happy to look at combinations of colours. The use of a water mark would be good. Open to suggestions.

Industry/Entity Type

Home Inspection

```html
<!DOCTYPE html>
<html lang="en">
<head>
<meta charset="utf-8">
<title>Steadfast Property Reviews — Stationery</title>
<link href="https://fonts.googleapis.com/css2?family=Questrial&family=Open+Sans:wght@400;600&display=swap" rel="stylesheet">
<style>
  :root {
    --blue: #0d4fa8;
    --slate: #5b7a89;
    --ink: #1f1f1f;
    --paper: #ffffff;
    --black: #0b0b0b;
    --stage: #5a3b22;
    --label: #f3e9de;
  }
  * { box-sizing: border-box; margin: 0; padding: 0; }
  html, body { width: 1200px; height: 531px; overflow: hidden; }
  body { background: var(--stage); font-family: "Open Sans", sans-serif; color: var(--ink); position: relative; }

  .sheet { position: absolute; top: 33px; width: 326px; height: 421px; background: var(--paper); box-shadow: 0 1px 4px rgba(0,0,0,.35); }
  .sheet--letter { left: 38px; }
  .sheet--fax { left: 375px; }

  .brand { position: absolute; display: flex; flex-direction: column; align-items: flex-start; gap: 3px; }
  .brand__mark { width: 14px; height: 14px; background: var(--blue); }
  .brand__name { font-family: "Questrial", sans-serif; color: var(--blue); font-size: 7px; line-height: 1.15; width: 70px; }
  .sheet .brand { left: 9px; top: 8px; align-items: center; }
  .sheet .brand__name { text-align: center; }

  .contact { position: absolute; left: 236px; top: 11px; border-left: 1px solid var(--ink); padding-left: 4px; font-size: 5.2px; line-height: 8px; }
  .contact li { list-style: none; display: flex; align-items: center; gap: 3px; white-space: nowrap; }
  .contact svg { width: 4px; height: 4px; fill: var(--ink); flex: none; }

  .footer { position: absolute; left: 0; right: 0; bottom: 0; height: 24px; }
  .footer__mark { position: absolute; left: 10px; top: 0; width: 12px; height: 12px; background: var(--blue); }
  .footer__address { position: absolute; right: 10px; top: 3px; font-size: 6.6px; letter-spacing: .2px; }
  .footer__rule { position: absolute; left: 0; right: 0; bottom: 7px; height: 2px; background: var(--slate); }
  .footer__band { position: absolute; left: 0; right: 0; bottom: 0; height: 5px; background: var(--blue); }

  .fax__title { position: absolute; left: 7px; top: 90px; font-size: 19px; font-weight: 400; }
  .fax__fields { position: absolute; left: 7px; top: 126px; width: 283px; display: grid; grid-template-columns: 158px 125px; row-gap: 8px; }
  .fax__field { font-size: 5px; height: 10px; border-bottom: 1px solid var(--ink); padding-top: 1px; }
  .fax__checks { position: absolute; left: 7px; top: 232px; display: flex; gap: 15px; font-size: 5px; }
  .fax__check { display: flex; align-items: center; gap: 3px; }
  .fax__box { width: 7px; height: 7px; border: 1px solid var(--ink); }

  .envelope { position: absolute; background: var(--paper); box-shadow: 0 1px 4px rgba(0,0,0,.35); overflow: hidden; }
  .envelope--black { left: 786px; top: 39px; width: 338px; height: 161px; }
  .envelope--blue { left: 775px; top: 110px; width: 337px; height: 161px; background: linear-gradient(#f4f4f4, #e4e4e4); }
  .envelope__flap { position: absolute; left: 0; top: 0; width: 100%; height: 64px; }
  .envelope__flap-name { position: absolute; left: 0; right: 0; top: 18px; text-align: center; font-family: "Questrial", sans-serif; color: var(--paper); font-size: 10px; }
  .envelope--front { left: 750px; top: 191px; width: 364px; height: 162px; background: linear-gradient(90deg, #ffffff 40%, #e9e9e9); }
  .envelope--front .brand { left: 10px; top: 6px; align-items: center; }
  .envelope--front .brand__name { text-align: center; }
  .envelope__address { position: absolute; left: 10px; top: 54px; font-size: 5.6px; }
  .envelope__footer { position: absolute; left: 0; right: 0; bottom: 0; height: 20px; }
  .envelope__footer .footer__mark { left: 10px; top: 0; width: 11px; height: 11px; }
  .envelope__web { position: absolute; left: 27px; top: 3px; font-size: 6px; }
  .envelope__footer .footer__rule { bottom: 6px; }
  .envelope__footer .footer__band { height: 4px; }

  .card { position: absolute; top: 381px; width: 134px; height: 75px; box-shadow: 0 1px 3px rgba(0,0,0,.35); overflow: hidden; }
  .card--front { left: 721px; background: linear-gradient(90deg, #fff 45%, #e6e6e6); }
  .card--front .brand { left: 4px; top: 4px; align-items: center; gap: 2px; }
  .card--front .brand__mark { width: 9px; height: 9px; }
  .card--front .brand__name { font-size: 5px; width: 42px; text-align: center; }
  .card__person { position: absolute; left: 70px; top: 25px; font-size: 5px; line-height: 5.6px; }
  .card__person strong { display: block; font-weight: 400; font-size: 5.6px; }
  .card__person small { display: block; font-size: 3.6px; margin-bottom: 3px; }
  .card__person span { display: block; font-size: 3.6px; line-height: 4.6px; }
  .card__rule { position: absolute; left: 0; right: 0; bottom: 2px; height: 1px; background: var(--slate); }
  .card--blue { left: 866px; background: var(--blue); }
  .card--slate { left: 1006px; background: var(--slate); }
  .card__name { position: absolute; left: 0; right: 0; top: 19px; text-align: center; font-family: "Questrial", sans-serif; color: var(--paper); font-size: 11px; line-height: 1.2; }
  .card__web { position: absolute; left: 0; right: 0; bottom: 10px; text-align: center; color: var(--paper); font-size: 5.6px; font-weight: 600; }

  .option-label { position: absolute; top: 472px; font-family: "Open Sans", sans-serif; color: var(--label); font-size: 23px; }
  .option-label--letter { left: 141px; }
  .option-label--fax { left: 487px; }
</style>
</head>
<body>

  <section class="sheet sheet--letter" aria-label="Letterhead">
    <div class="brand"><span class="brand__mark"></span><span class="brand__name">Steadfast Property Reviews</span></div>
    <ul class="contact">
      <li><svg viewBox="0 0 10 10"><circle cx="5" cy="5" r="5"/></svg>555-010-2040</li>
      <li><svg viewBox="0 0 10 10"><circle cx="5" cy="5" r="5"/></svg>555-010-2041</li>
      <li><svg viewBox="0 0 10 10"><rect y="2" width="10" height="6"/></svg>hello@steadfastreviews.com</li>
      <li><svg viewBox="0 0 10 10"><circle cx="5" cy="5" r="5"/></svg>www.steadfastreviews.com</li>
    </ul>
    <div class="footer">
      <span class="footer__mark"></span>
      <span class="footer__address">Street Name, City Name State Zipcode</span>
      <span class="footer__rule"></span><span class="footer__band"></span>
    </div>
  </section>

  <section class="sheet sheet--fax" aria-label="Fax cover sheet">
    <div class="brand"><span class="brand__mark"></span><span class="brand__name">Steadfast Property Reviews</span></div>
    <ul class="contact">
      <li><svg viewBox="0 0 10 10"><circle cx="5" cy="5" r="5"/></svg>555-010-2040</li>
      <li><svg viewBox="0 0 10 10"><circle cx="5" cy="5" r="5"/></svg>555-010-2041</li>
      <li><svg viewBox="0 0 10 10"><rect y="2" width="10" height="6"/></svg>hello@steadfastreviews.com</li>
      <li><svg viewBox="0 0 10 10"><circle cx="5" cy="5" r="5"/></svg>www.steadfastreviews.com</li>
    </ul>
    <h1 class="fax__title">FAX</h1>
    <div class="fax__fields">
      <div class="fax__field">To :</div><div class="fax__field">From :</div>
      <div class="fax__field">Fax :</div><div class="fax__field">Pages :</div>
      <div class="fax__field">Phone :</div><div class="fax__field">Date :</div>
      <div class="fax__field">Re :</div><div class="fax__field">CC :</div>
    </div>
    <div class="fax__checks">
      <span class="fax__check"><span class="fax__box"></span>Urgent</span>
      <span class="fax__check"><span class="fax__box"></span>For Review</span>
      <span class="fax__check"><span class="fax__box"></span>Please Comment</span>
      <span class="fax__check"><span class="fax__box"></span>Please Reply</span>
      <span class="fax__check"><span class="fax__box"></span>Please Recycle</span>
    </div>
    <div class="footer">
      <span class="footer__mark"></span>
      <span class="footer__address">Street Name, City Name State Zipcode</span>
      <span class="footer__rule"></span><span class="footer__band"></span>
    </div>
  </section>

  <section class="envelope envelope--black" aria-label="Envelope back, black flap">
    <svg class="envelope__flap" viewBox="0 0 338 64" preserveAspectRatio="none"><path d="M0 0H338V30Q175 78 0 30Z" fill="var(--black)"/></svg>
    <span class="envelope__flap-name">Steadfast Property Reviews</span>
  </section>

  <section class="envelope envelope--blue" aria-label="Envelope back, blue flap">
    <svg class="envelope__flap" viewBox="0 0 337 64" preserveAspectRatio="none"><path d="M0 0H337V36Q170 90 0 36Z" fill="var(--blue)"/></svg>
    <span class="envelope__flap-name">Steadfast Property Reviews</span>
  </section>

  <section class="envelope envelope--front" aria-label="Envelope front">
    <div class="brand"><span class="brand__mark"></span><span class="brand__name">Steadfast Property Reviews</span></div>
    <p class="envelope__address">Street Name, City Name, State Zipcode</p>
    <div class="envelope__footer">
      <span class="footer__mark"></span>
      <span class="envelope__web">www.steadfastreviews.com</span>
      <span class="footer__rule"></span><span class="footer__band"></span>
    </div>
  </section>

  <section class="card card--front" aria-label="Business card front">
    <div class="brand"><span class="brand__mark"></span><span class="brand__name">Steadfast Property Reviews</span></div>
    <div class="card__person">
      <strong>Your Name</strong>
      <small>Title</small>
      <span>555-010-2040</span>
      <span>555-010-2041</span>
      <span>hello@steadfastreviews.com</span>
      <span>www.steadfastreviews.com</span>
      <span>Street Name, City Name,</span>
      <span>State Zipcode</span>
    </div>
    <span class="card__rule"></span>
  </section>

  <section class="card card--blue" aria-label="Business card back, blue">
    <p class="card__name">Steadfast<br>Property Reviews</p>
    <p class="card__web">www.steadfastreviews.com</p>
  </section>

  <section class="card card--slate" aria-label="Business card back, slate">
    <p class="card__name">Steadfast<br>Property Reviews</p>
    <p class="card__web">www.steadfastreviews.com</p>
  </section>

  <p class="option-label option-label--letter">Option-1</p>
  <p class="option-label option-label--fax">Option-1</p>

</body>
</html>
```